To design a brand identity that is simple and creative with 'Valtor' as the brand name, I like modern simple fonts like helvetica neue, I want to print both sides of the card, I am open to dark front and white back, but the design needs to transfer well to letter heads and email signatures, I am looking for sophisticated and elegant, but open minded about clever and off the wall, I do not do 'boring' Valtor Holdings is the mother company for a small group, specialising in Management & consulting, Software development and construction, we have a high level of integrity, we are transparent and accountable for what we do. my images are provided as a guide only, Im not expecting them to be just copied, Im looking for a creator and passionate thinker, who will put life into their work.

Target Market(s)

usually business minded people who are looking for something different in me, such as leadership, confidence and focus with thinking that is per haps a little outside the box..

Industry/Entity Type

Construction

Requirements
Must have
• clean, minmalistic
Nice to have
• custom logo
Should not have
• boring, traditional

```html
<!DOCTYPE html>
<html lang="en">
<head>
<meta charset="utf-8">
<title>Valtor – Business Card, Front and Back</title>
<link rel="stylesheet" href="https://fonts.googleapis.com/css2?family=Questrial&family=Damion&display=swap">
<style>
  :root {
    --stage: #3a3634;
    --ink: #1b1b1b;
    --paper: #ffffff;
    --ice-light: #d6eef8;
    --ice: #8fd0ec;
    --ice-deep: #3fb3e0;
    --accent-red: #e23a2a;
    --accent-orange: #f0a646;
    --card-dark: #2b2a2a;
    --card-dark-glow: #4a4847;
    --muted-light: #e6e6e6;
  }
  * { margin: 0; padding: 0; box-sizing: border-box; }
  html, body { width: 1200px; height: 1000px; overflow: hidden; }
  body {
    background: var(--stage);
    font-family: "Questrial", "Helvetica Neue", Arial, sans-serif;
    position: relative;
  }

  /* ---------- Front card (portrait) ---------- */
  .card-front {
    position: absolute;
    left: 90px; top: 140px;
    width: 430px; height: 704px;
    background: linear-gradient(to bottom, var(--paper) 0%, var(--paper) 38%, var(--ice-light) 62%, var(--ice) 100%);
    overflow: hidden;
  }
  .brand-front {
    position: absolute;
    top: 62px; right: 46px;
    display: flex; align-items: center; gap: 16px;
  }
  .brand-mark {
    width: 78px; height: 78px; border-radius: 50%;
    background: var(--accent-orange);
  }
  .brand-name {
    font-size: 70px; line-height: 1; color: var(--ink); letter-spacing: 1px;
  }
  .web-front {
    position: absolute; top: 150px; right: 48px;
    font-size: 19px; color: var(--ink); letter-spacing: 0.5px;
  }
  .web-prefix { color: var(--accent-red); }
  .tagline {
    position: absolute; top: 218px; right: 40px;
    font-family: "Damion", cursive;
    font-size: 30px; line-height: 1.3; color: var(--ink);
    text-align: right;
    transform: rotate(-5deg);
  }
  .ice-scene {
    position: absolute; left: 0; bottom: 0;
    width: 100%; height: 230px;
    background: linear-gradient(to bottom, rgba(143,208,236,0) 0%, var(--ice) 40%, var(--ice-deep) 100%);
  }
  .contact {
    position: absolute; right: 46px; top: 470px;
    text-align: right; color: var(--ink);
  }
  .contact-name { font-size: 32px; margin-bottom: 16px; }
  .contact-line {
    display: flex; justify-content: flex-end; align-items: center; gap: 8px;
    font-size: 16px; margin-bottom: 10px;
  }
  .contact-icon { width: 15px; height: 15px; flex: none; }

  /* ---------- Back card (landscape) ---------- */
  .card-back {
    position: absolute;
    left: 590px; top: 330px;
    width: 560px; height: 342px;
    background: radial-gradient(ellipse at 45% 45%, var(--card-dark-glow) 0%, var(--card-dark) 70%);
  }
  .brand-back {
    position: absolute; top: 88px; left: 0; width: 100%;
    display: flex; justify-content: center; align-items: center; gap: 20px;
  }
  .brand-back .brand-mark { width: 92px; height: 92px; }
  .brand-back .brand-name { font-size: 86px; color: var(--paper); }
  .services {
    position: absolute; top: 212px; left: 0; width: 100%;
    text-align: center; font-size: 15px; letter-spacing: 2px; color: var(--muted-light);
  }
  .services .dot { color: var(--accent-red); margin: 0 6px; }
  .web-back {
    position: absolute; top: 242px; left: 0; width: 100%;
    text-align: center; font-size: 19px; color: var(--muted-light); letter-spacing: 0.5px;
  }
</style>
</head>
<body>

  <section class="card-front" aria-label="Card front">
    <div class="ice-scene" role="img" aria-label="Photograph of a blue glacier ice wall above water"></div>

    <div class="brand-front">
      <span class="brand-mark" aria-hidden="true"></span>
      <span class="brand-name">valtor</span>
    </div>
    <p class="web-front"><span class="web-prefix">www.</span>valtor.holdings</p>

    <p class="tagline">pure passion...<br>clarity in development</p>

    <div class="contact">
      <p class="contact-name">marcus</p>
      <p class="contact-line">+ 61 0400 555 012
        <svg class="contact-icon" viewBox="0 0 24 24" aria-hidden="true">
          <path fill="#e23a2a" d="M6.6 10.8a15.1 15.1 0 0 0 6.6 6.6l2.2-2.2a1 1 0 0 1 1-.25 11.4 11.4 0 0 0 3.6.6 1 1 0 0 1 1 1V20a1 1 0 0 1-1 1A17 17 0 0 1 3 4a1 1 0 0 1 1-1h3.5a1 1 0 0 1 1 1c0 1.25.2 2.45.6 3.6a1 1 0 0 1-.25 1z"/>
        </svg>
      </p>
      <p class="contact-line">marcus@valtor.holdings
        <svg class="contact-icon" viewBox="0 0 24 24" aria-hidden="true">
          <rect x="2" y="5" width="20" height="14" rx="1.5" fill="#e23a2a"/>
          <path d="M2.5 6l9.5 7 9.5-7" fill="none" stroke="#ffffff" stroke-width="1.6"/>
        </svg>
      </p>
    </div>
  </section>

  <section class="card-back" aria-label="Card back">
    <div class="brand-back">
      <span class="brand-mark" aria-hidden="true"></span>
      <span class="brand-name">valtor</span>
    </div>
    <p class="services">management<span class="dot">•</span>software<span class="dot">•</span>construction</p>
    <p class="web-back"><span class="web-prefix">www.</span>valtor.holdings</p>
  </section>

</body>
</html>
```